Brimo, a service provider dedicated to improving the performance of a website

Brimo offers optimization and performance improvement for all types of websites (showcase sites, e-commerce, ...), with the aim of improving their ranking on Searvo and their customer transformation rate. The main benefits consist in optimizing the factors of a site. In addition, we also offer content creation (description of product sheets, services, ...), Searvo Ads campaign management, migration version for Prestashop / Wordpress, etc. The design must be a fresh image, dynamic, why not "fun", but also serious. No favorite color, carte blanche on this point;)

```html
<!DOCTYPE html>
<html lang="en">
<head>
<meta charset="utf-8">
<title>Brimo — Business Card</title>
<link href="https://fonts.googleapis.com/css2?family=Raleway:ital,wght@0,400;0,500;0,700;0,800;1,400&display=swap" rel="stylesheet">
<style>
  :root {
    --stage: #15152a;
    --brand-blue: #3a53a0;
    --ink-blue: #2f48a3;
    --card-white: #ffffff;
    --text-grey: #6f6f78;
    --white: #ffffff;
  }
  * { margin: 0; padding: 0; box-sizing: border-box; }
  html, body { width: 1200px; height: 1200px; overflow: hidden; }
  body {
    position: relative;
    background: var(--stage);
    font-family: "Raleway", sans-serif;
  }
  .card {
    position: absolute;
    top: 310px;
    width: 460px;
    height: 263px;
    border-radius: 22px;
    overflow: hidden;
  }
  .card--front { left: 120px; background: var(--card-white); color: var(--text-grey); }
  .card--back { left: 620px; background: var(--brand-blue); color: var(--white); }

  .holder-name {
    position: absolute; left: 34px; top: 30px;
    font-size: 22px; font-weight: 700; color: var(--ink-blue);
  }
  .contact-list {
    position: absolute; left: 34px; top: 72px;
    list-style: none; font-size: 13px; line-height: 19px;
  }
  .social {
    position: absolute; left: 34px; top: 170px;
    display: flex; align-items: center; gap: 6px;
    font-size: 13px; font-style: italic;
  }
  .social-label { margin-right: 6px; }
  .social-dot { width: 18px; height: 18px; border-radius: 50%; background: var(--ink-blue); }
  .front-wordmark {
    position: absolute; right: 30px; bottom: 22px;
    font-size: 54px; font-weight: 800; color: var(--ink-blue); letter-spacing: -1px;
  }

  .back-wordmark {
    position: absolute; left: 0; right: 0; top: 52px;
    text-align: center; font-size: 88px; font-weight: 800; letter-spacing: -2px;
  }
  .tagline {
    position: absolute; left: 0; right: 0; top: 160px;
    text-align: center; font-size: 18px; font-style: italic;
  }
  .website {
    position: absolute; left: 0; right: 0; top: 196px;
    text-align: center; font-size: 14px; letter-spacing: 1px;
  }

  .brand-band {
    position: absolute; left: 0; bottom: 0;
    width: 1200px; height: 302px; background: var(--brand-blue);
  }
  .band-wordmark {
    position: absolute; left: 72px; bottom: 44px;
    font-size: 56px; font-weight: 800; color: var(--white); letter-spacing: -1px;
  }
</style>
</head>
<body>
  <section class="card card--front" aria-label="Card front">
    <h1 class="holder-name">Nadia Verlane</h1>
    <ul class="contact-list">
      <li>(555) 214-3390</li>
      <li>nadia@brimo.com</li>
      <li>418 Harbor Ln.</li>
      <li>Fairview OR 97024</li>
    </ul>
    <div class="social">
      <span class="social-label">follow us</span>
      <span class="social-dot"></span>
      <span class="social-dot"></span>
      <span class="social-dot"></span>
      <span class="social-dot"></span>
    </div>
    <div class="front-wordmark">Brimo</div>
  </section>

  <section class="card card--back" aria-label="Card back">
    <div class="back-wordmark">Brimo</div>
    <p class="tagline">“Optimize your website”</p>
    <p class="website">www.brimo.com</p>
  </section>

  <footer class="brand-band">
    <div class="band-wordmark">Brimo</div>
  </footer>
</body>
</html>
```